Unique Elegant Stationary Set

Prepare a unique eye catching stationary set consisting of :
(1) Letterhead
(2) A3 Envelope
(3) Business Card
(4) Email Signature Banner

Package to be elegant, modern, and designers not only to think of design or colors but also materials could make a big difference, embossing, debossing, glossy, matt ....etc.

I attached both our new logos (Stacked or Linear) noting you may use any of them but you cant modify anything in the logos. Also attached our final draft portfolio to see what type of projects we work on and i also have here a glimmerboard page link showing the direction we want: https://www.glimmerboard.example/dorvanmelik/business-card-design/

Target Market(s)

VVIP / Elite Developers

Industry/Entity Type

Architecture

Font styles to use
Sans Serif
Other font styles liked:
• unitext

Requirements
Should not have
• too many colors, or being busy in general. We want something pleasing to the eye

```html
<!DOCTYPE html>
<html lang="en">
<head>
<meta charset="utf-8">
<title>Valmora Studio — Business Card</title>
<link rel="stylesheet" href="https://fonts.googleapis.com/css2?family=Lato:wght@400;700&family=Montserrat:wght@800&display=swap">
<style>
  :root {
    --backdrop: #3a3a3a;
    --card-black: #1b1b1b;
    --mark-grey: #2e2e2e;
    --card-white: #ffffff;
    --ink: #111111;
    --accent-red: #c62026;
    --rule: #4a4a4a;
  }
  * { box-sizing: border-box; margin: 0; padding: 0; }
  html, body { width: 1200px; height: 694px; overflow: hidden; }
  body {
    background: var(--backdrop);
    font-family: "Lato", Arial, sans-serif;
    position: relative;
  }
  .card {
    position: absolute;
    top: 198px;
    width: 520px;
    height: 297px;
    border-radius: 22px;
    overflow: hidden;
  }
  .card-back { left: 50px; background: var(--card-black); }
  .card-front { left: 630px; background: var(--card-white); color: var(--ink); }

  .wordmark {
    font-family: "Montserrat", Arial, sans-serif;
    font-weight: 800;
    text-transform: uppercase;
    line-height: 1;
  }
  .wordmark-main { display: block; }
  .wordmark-sub { display: block; }

  .brand-back {
    position: absolute;
    left: 0; right: 0;
    top: 102px;
    text-align: center;
    color: var(--mark-grey);
  }
  .brand-back .wordmark-main { font-size: 58px; letter-spacing: 2px; }
  .brand-back .wordmark-sub { font-size: 20px; letter-spacing: 22px; margin-top: 12px; padding-left: 22px; }

  .brand-front {
    position: absolute;
    top: 34px;
    right: 34px;
    text-align: left;
    color: var(--ink);
  }
  .brand-front .wordmark-main { font-size: 40px; letter-spacing: 1px; }
  .brand-front .wordmark-sub { font-size: 14px; letter-spacing: 16px; margin-top: 8px; }

  .rule { position: absolute; height: 1px; background: var(--rule); }
  .rule-long { top: 128px; left: 196px; right: 30px; }
  .rule-short { top: 184px; left: 32px; width: 150px; }

  .holder { position: absolute; left: 32px; top: 126px; }
  .holder-name {
    font-weight: 700;
    font-size: 21px;
    letter-spacing: 0.3px;
    text-transform: uppercase;
    color: var(--accent-red);
    line-height: 1.1;
  }
  .holder-role { font-size: 13px; margin-top: 5px; }

  .contacts {
    position: absolute;
    left: 32px;
    top: 196px;
    list-style: none;
    font-size: 13px;
  }
  .contacts li { display: flex; align-items: center; gap: 10px; height: 22px; }
  .contacts svg { width: 14px; height: 14px; flex: none; }

  .address {
    position: absolute;
    right: 34px;
    top: 146px;
    text-align: right;
    font-size: 13.5px;
    line-height: 1.5;
  }
  .edge-band { position: absolute; left: 0; bottom: 0; width: 520px; height: 40px; }
</style>
</head>
<body>
  <section class="card card-back" aria-label="Card back">
    <p class="wordmark brand-back">
      <span class="wordmark-main">Valmora</span>
      <span class="wordmark-sub">Studio</span>
    </p>
  </section>

  <section class="card card-front" aria-label="Card front">
    <p class="wordmark brand-front">
      <span class="wordmark-main">Valmora</span>
      <span class="wordmark-sub">Studio</span>
    </p>
    <div class="rule rule-long"></div>

    <div class="holder">
      <h1 class="holder-name">Elias Varno</h1>
      <p class="holder-role">Managing Director</p>
    </div>
    <div class="rule rule-short"></div>

    <ul class="contacts">
      <li>
        <svg viewBox="0 0 16 16" aria-hidden="true"><path fill="#c62026" d="M3.6 1.5l2.3 2.3-1.2 1.8c.9 2 2.5 3.6 4.5 4.5l1.8-1.2 2.3 2.3-1.5 2.3C6.8 13.2 2.8 9.2 1.3 4.2z"/></svg>
        044-987 654 321
      </li>
      <li>
        <svg viewBox="0 0 16 16" aria-hidden="true"><rect x="1" y="3" width="14" height="10" fill="#c62026"/><path d="M1 3l7 6 7-6" fill="none" stroke="#fff" stroke-width="1.2"/></svg>
        info@valmorastudio.example
      </li>
      <li>
        <svg viewBox="0 0 16 16" aria-hidden="true"><circle cx="8" cy="8" r="7" fill="#c62026"/><path d="M1 8h14M8 1c-3 3.5-3 10.5 0 14M8 1c3 3.5 3 10.5 0 14" fill="none" stroke="#fff" stroke-width="1"/></svg>
        www.valmorastudio.example
      </li>
    </ul>

    <p class="address">421, Address line goes here<br>45452, Country name</p>

    <svg class="edge-band" viewBox="0 0 520 40" aria-hidden="true">
      <polygon points="290,30 312,16 520,16 520,40 290,40" fill="#c62026"/>
      <polygon points="290,40 302,32 520,32 520,40" fill="#111111"/>
    </svg>
  </section>
</body>
</html>
```